Automotive component supplier needs a business card design

We need a business card design for our company called Velmar Global Components Ltd based in the UK. We are a supplier of interior and exterior components to premium car manufacturers such as Corvane Hale, Durrant Fyfe, Maxtorn and Valdessimo. We would like to see a modern business card design that uses the colour blue.

Target Market(s)

Premium automotive car manufacturers.

Industry/Entity Type

Automotive

Contact Information for Business Card

Company Name : Velmar Global Components Limited
Address: 17 Tamsey Yard, Upper Drisk, Warwick, CV31 8RJ, United Kingdom
Web Address : www.velmarparts-example.co.uk

Font styles to use
Other font styles liked:
• Helvetica

Colors
3176b5
0255a3
85acd3
cfdeed
cee9f5
85cae6
34a6d7
0692cd
9bcb3c

Requirements
Must have
• Clear company logo and a mixture of blue colours.
Nice to have
• A high quality modern image.
Should not have
• Multiple colours.

```html
<!DOCTYPE html>
<html lang="en">
<head>
<meta charset="utf-8">
<title>Velmar Global Components – Business Card</title>
<link rel="stylesheet" href="https://fonts.googleapis.com/css2?family=Open+Sans:wght@400;600&family=Oswald:wght@500&family=Montserrat:wght@700&display=swap">
<style>
  :root {
    --backdrop: #e9e6e1;
    --band-dark: #0b5a84;
    --band-light: #1c9ad6;
    --accent: #34a6d7;
    --logo-blue: #1e9ad6;
    --paper: #ffffff;
    --text-grey: #555a5e;
    --white: #ffffff;
  }
  * { margin: 0; padding: 0; box-sizing: border-box; }
  html, body {
    width: 1200px;
    height: 831px;
    overflow: hidden;
    background: var(--backdrop);
  }
  .card {
    position: absolute;
    left: 100px;
    top: 132px;
    width: 1000px;
    height: 567px;
    background: var(--paper);
    box-shadow: 0 6px 18px rgba(0,0,0,0.18);
    overflow: hidden;
    font-family: "Open Sans", Arial, sans-serif;
  }
  .card-header {
    position: absolute;
    left: 0; top: 0;
    width: 100%;
    height: 243px;
    background: var(--band-dark);
  }
  .brand-name {
    position: absolute;
    left: 52px;
    top: 52px;
    font-family: "Montserrat", Arial, sans-serif;
    font-weight: 700;
    font-size: 66px;
    letter-spacing: 1px;
    line-height: 1;
    color: var(--logo-blue);
  }
  .company-line {
    position: absolute;
    right: 52px;
    top: 194px;
    font-family: "Oswald", "Arial Narrow", sans-serif;
    font-weight: 500;
    font-size: 27px;
    letter-spacing: 1.6px;
    line-height: 1;
    color: var(--white);
    text-transform: uppercase;
    white-space: nowrap;
  }
  .company-line .highlight { color: var(--accent); }
  .contact {
    position: absolute;
    display: flex;
    align-items: center;
    font-size: 25px;
    color: var(--text-grey);
    line-height: 1;
    white-space: nowrap;
  }
  .contact svg { width: 24px; height: 24px; fill: var(--accent); flex: none; }
  .contact-left { left: 40px; }
  .contact-left svg { margin-right: 22px; }
  .contact-right { right: 54px; }
  .contact-right svg { margin-left: 20px; }
  .phone { top: 408px; }
  .mobile { top: 444px; }
  .email { top: 408px; }
  .web { top: 444px; }
  .address-band {
    position: absolute;
    left: 0;
    bottom: 0;
    width: 100%;
    height: 72px;
    background: var(--band-light);
    display: flex;
    align-items: center;
    justify-content: space-between;
    padding: 0 54px 0 52px;
    color: var(--white);
    font-size: 27px;
    white-space: nowrap;
  }
  .address-band svg { width: 26px; height: 30px; fill: var(--white); }
</style>
</head>
<body>
  <div class="card">
    <div class="card-header">
      <div class="brand-name">VELMAR</div>
      <div class="company-line">Velmar Global <span class="highlight">Components Limited</span></div>
    </div>

    <div class="contact contact-left phone">
      <svg viewBox="0 0 24 24" aria-hidden="true"><path d="M6.6 10.8a15.1 15.1 0 0 0 6.6 6.6l2.2-2.2c.3-.3.7-.4 1-.2 1.1.4 2.3.6 3.6.6.6 0 1 .4 1 1V20c0 .6-.4 1-1 1A17 17 0 0 1 3 4c0-.6.4-1 1-1h3.5c.6 0 1 .4 1 1 0 1.3.2 2.5.6 3.6.1.3 0 .7-.2 1z"/></svg>
      <span>(555) 018-2740</span>
    </div>
    <div class="contact contact-left mobile">
      <svg viewBox="0 0 24 24" aria-hidden="true"><path d="M7 1h10a2 2 0 0 1 2 2v18a2 2 0 0 1-2 2H7a2 2 0 0 1-2-2V3a2 2 0 0 1 2-2zm0 3v14h10V4zm5 15.2a1.1 1.1 0 1 0 0 2.2 1.1 1.1 0 0 0 0-2.2z"/></svg>
      <span>(555) 018-3961</span>
    </div>

    <div class="contact contact-right email">
      <span>hello@vgc-mail.com</span>
      <svg viewBox="0 0 24 24" aria-hidden="true"><path d="M2 5h20v14H2zm2 2v.5l8 5 8-5V7zm0 2.8V17h16V9.8l-8 5z"/></svg>
    </div>
    <div class="contact contact-right web">
      <span>www.velmarparts-example.co.uk</span>
      <svg viewBox="0 0 24 24" aria-hidden="true"><path d="M12 2a10 10 0 1 0 0 20 10 10 0 0 0 0-20zm6.9 6h-2.9a15 15 0 0 0-1.3-3.6A8 8 0 0 1 18.9 8zM12 4c.8 1.2 1.5 2.5 1.9 4h-3.8c.4-1.5 1.1-2.8 1.9-4zM4.3 14a8 8 0 0 1 0-4h3.4a16 16 0 0 0 0 4zm.8 2h2.9c.3 1.3.8 2.5 1.3 3.6A8 8 0 0 1 5.1 16zM8 8H5.1a8 8 0 0 1 4.2-3.6C8.8 5.5 8.3 6.7 8 8zm4 12c-.8-1.2-1.5-2.5-1.9-4h3.8c-.4 1.5-1.1 2.8-1.9 4zm2.3-6H9.7a14 14 0 0 1 0-4h4.6a14 14 0 0 1 0 4zm.4 5.6c.5-1.1 1-2.3 1.3-3.6h2.9a8 8 0 0 1-4.2 3.6zm1.6-5.6a16 16 0 0 0 0-4h3.4a8 8 0 0 1 0 4z"/></svg>
    </div>

    <div class="address-band">
      <span>17 Tamsey Yard, Upper Drisk, Warwick, CV31 8RJ, United Kingdom</span>
      <svg viewBox="0 0 20 24" aria-hidden="true"><path d="M10 0a8 8 0 0 0-8 8c0 6 8 16 8 16s8-10 8-16a8 8 0 0 0-8-8zm0 11a3 3 0 1 1 0-6 3 3 0 0 1 0 6z"/></svg>
    </div>
  </div>
</body>
</html>
```